Business Card Design Project

We are an incubator company that helps young entrepreneur to launch new ideas into the market. We will be targeting investors or likewise; Angels, young entrepreneurs and technopreneurs.

Our logo is being tasked by artswarm to design, therefore there is no logo for now.
You can us Lanternfield Pte Ltd as the logo for the time being.

Please let us have some versions of modern and yet professional designs; for words, you can indicate e.g (address), (Title)

thanks

Target Market(s)

young entrepreneurs
angels, investors

Industry/Entity Type

Business

Colors
3176b5
ffffff

Requirements
Must have
• able to project out our name; Lanternfield
Should not have
• Nothing childish or cartoon

```html
<!DOCTYPE html>
<html lang="en">
<head>
<meta charset="utf-8">
<title>Lanternfield Business Card</title>
<link href="https://fonts.googleapis.com/css2?family=Roboto:wght@400;500;700;900&display=swap" rel="stylesheet">
<style>
  :root {
    --brand-blue: #3176b5;
    --brand-deep: #1f5f9e;
    --card-white: #ffffff;
    --stage: #eef0f2;
    --ink: #2b2b2b;
    --muted: #555a60;
  }
  * { box-sizing: border-box; margin: 0; padding: 0; }
  html, body { width: 1200px; height: 1001px; overflow: hidden; }
  body {
    background: var(--stage);
    font-family: "Roboto", Arial, sans-serif;
    display: flex;
    flex-direction: column;
    align-items: center;
    justify-content: center;
    gap: 60px;
  }
  .card {
    position: relative;
    width: 700px;
    height: 400px;
    background: var(--card-white);
    box-shadow: 0 2px 10px rgba(0,0,0,0.08);
    overflow: hidden;
  }
  .wordmark { display: flex; flex-direction: column; align-items: flex-start; }
  .wordmark-row { display: flex; align-items: center; gap: 14px; }
  .wordmark-square {
    width: 44px; height: 44px;
    background: var(--brand-blue);
    border-radius: 8px;
  }
  .wordmark-name {
    font-weight: 900;
    font-size: 40px;
    letter-spacing: 1px;
    color: var(--brand-blue);
    text-transform: uppercase;
  }
  .wordmark-tagline {
    margin-top: 4px;
    margin-left: 58px;
    font-weight: 500;
    font-size: 11px;
    letter-spacing: 3.4px;
    color: var(--muted);
    text-transform: uppercase;
    white-space: nowrap;
  }
  .card-front .wordmark {
    position: absolute;
    left: 50%; top: 50%;
    transform: translate(-50%, -50%);
  }
  .card-back .wordmark { position: absolute; left: 48px; top: 48px; }
  .card-back .wordmark-name { font-size: 32px; }
  .card-back .wordmark-square { width: 36px; height: 36px; }
  .card-back .wordmark-tagline { margin-left: 50px; font-size: 9px; letter-spacing: 2.8px; }
  .contact {
    position: absolute;
    left: 330px; top: 170px;
    color: var(--ink);
  }
  .contact-name { font-weight: 700; font-size: 20px; color: var(--brand-blue); }
  .contact-title { font-size: 13px; color: var(--muted); margin-bottom: 16px; }
  .contact-list { list-style: none; }
  .contact-item {
    display: flex; align-items: center; gap: 10px;
    font-size: 14px; font-weight: 500;
    margin-bottom: 9px;
    white-space: nowrap;
  }
  .contact-icon { width: 16px; height: 16px; fill: var(--brand-deep); flex: none; }
</style>
</head>
<body>
  <section class="card card-front">
    <div class="wordmark">
      <div class="wordmark-row">
        <span class="wordmark-square"></span>
        <span class="wordmark-name">Lanternfield</span>
      </div>
      <span class="wordmark-tagline">Launching Bold Ideas Ahead</span>
    </div>
  </section>

  <section class="card card-back">
    <div class="wordmark">
      <div class="wordmark-row">
        <span class="wordmark-square"></span>
        <span class="wordmark-name">Lanternfield</span>
      </div>
      <span class="wordmark-tagline">Launching Bold Ideas Ahead</span>
    </div>

    <div class="contact">
      <p class="contact-name">Your Name</p>
      <p class="contact-title">Title</p>
      <ul class="contact-list">
        <li class="contact-item">
          <svg class="contact-icon" viewBox="0 0 16 16"><path d="M8 0a5.5 5.5 0 0 0-5.5 5.5C2.5 10 8 16 8 16s5.5-6 5.5-10.5A5.5 5.5 0 0 0 8 0zm0 8a2.5 2.5 0 1 1 0-5 2.5 2.5 0 0 1 0 5z"/></svg>
          Your Commercial or office address
        </li>
        <li class="contact-item">
          <svg class="contact-icon" viewBox="0 0 16 16"><path d="M3 1h3l1.5 4-2 1.3a9 9 0 0 0 4.2 4.2L11 8.5l4 1.5v3a2 2 0 0 1-2 2A13 13 0 0 1 1 3a2 2 0 0 1 2-2z"/></svg>
          00.00.00.0000
        </li>
        <li class="contact-item">
          <svg class="contact-icon" viewBox="0 0 16 16"><path d="M4 1h6l2 2v3H4zM2 7h12a1 1 0 0 1 1 1v5a1 1 0 0 1-1 1H2a1 1 0 0 1-1-1V8a1 1 0 0 1 1-1zm2 2v1h3V9z"/></svg>
          00.00.00.0000
        </li>
        <li class="contact-item">
          <svg class="contact-icon" viewBox="0 0 16 16"><path d="M1 3h14v10H1zm1.5 1.2V5l5.5 4 5.5-4v-.8L8 8z"/></svg>
          yourname@yourwebsite.com
        </li>
        <li class="contact-item">
          <svg class="contact-icon" viewBox="0 0 16 16"><path d="M8 0a8 8 0 1 0 0 16A8 8 0 0 0 8 0zm5.9 7.2h-2.6a12 12 0 0 0-1-5 6.3 6.3 0 0 1 3.6 5zM8 1.8c.8 1.1 1.5 3 1.6 5.4H6.4C6.5 4.8 7.2 2.9 8 1.8zM5.7 2.2a12 12 0 0 0-1 5H2.1a6.3 6.3 0 0 1 3.6-5zM2.1 8.8h2.6a12 12 0 0 0 1 5 6.3 6.3 0 0 1-3.6-5zM8 14.2c-.8-1.1-1.5-3-1.6-5.4h3.2c-.1 2.4-.8 4.3-1.6 5.4zm2.3-.4a12 12 0 0 0 1-5h2.6a6.3 6.3 0 0 1-3.6 5z"/></svg>
          www.yourwebsite.com
        </li>
      </ul>
    </div>
  </section>
</body>
</html>
```